Building Defect timeline illustration

We need an memorable illustration using iconography to plot the time frame for a building defects process. These are typically shown in single line format and not catchy. Designed to stand out. Powerpoint of the timeline attached. Colour blue to be dominant please.Can use building/construction imagery/icons.

Target Market(s)

Builders/Developers/General public

Industry/Entity Type

Property

Font styles to use
Sans Serif

Colors
0355a3
3176b5
ffffff

Requirements
Must have
• Visual appeal, ability to stick to the factual timeline.
Nice to have
• You could incorporate building/construction into the graphics- suggestion only.

```html
<!DOCTYPE html>
<html lang="en">
<head>
<meta charset="utf-8">
<title>Building Defect Bond Timeline</title>
<link href="https://fonts.googleapis.com/css2?family=Arimo:wght@400;700&display=swap" rel="stylesheet">
<style>
  :root {
    --blue: #1b75bc;
    --blue-deep: #0355a3;
    --grey-band: #bcbec0;
    --grey-rail: #6d6e71;
    --white: #ffffff;
    --ink: #111111;
  }
  html, body {
    margin: 0;
    padding: 0;
    width: 1200px;
    height: 1000px;
    overflow: hidden;
    background: var(--white);
    font-family: "Arimo", Arial, sans-serif;
  }
  .canvas { position: relative; width: 1200px; height: 1000px; }
  .panel {
    position: absolute; left: 162px; top: 194px;
    width: 841px; height: 595px;
    background: var(--blue);
    outline: 1px solid #2a3a4a;
  }
  .band {
    position: absolute; left: 162px; top: 484px;
    width: 841px; height: 133px;
    background: var(--grey-band);
  }
  .rail {
    position: absolute; left: 162px; top: 470px;
    width: 841px; height: 16px;
    background: var(--grey-rail);
  }
  .chevrons { position: absolute; left: 0; top: 0; }
  .step { position: absolute; top: 295px; width: 132px; margin-left: -66px; }
  .callout {
    position: relative;
    width: 90px; height: 112px;
    margin: 0 auto;
    background: var(--grey-band);
    border-radius: 10px;
    box-sizing: border-box;
    padding: 16px 6px 0;
    font-size: 9px; line-height: 12px;
    color: var(--ink);
    text-align: center;
  }
  .callout::after {
    content: ""; position: absolute; left: 50%; bottom: -24px;
    width: 12px; margin-left: -6px; height: 26px;
    background: var(--grey-band);
  }
  .badge {
    position: absolute; top: 135px; left: 50%;
    width: 88px; height: 88px; margin-left: -44px;
    border-radius: 50%;
    background: var(--white);
    border: 5px solid var(--blue);
    box-sizing: border-box;
    display: flex; align-items: center; justify-content: center;
    overflow: hidden;
  }
  .badge svg { display: block; }
  .badge .illustration {
    width: 100%; height: 100%;
    background: radial-gradient(circle at 50% 45%, #e9f1f8 0%, #a9c8e4 100%);
  }
  .label {
    position: absolute; top: 232px; left: 0; width: 132px;
    font-weight: 700; font-size: 11.5px; line-height: 14px;
    text-align: center; color: var(--ink);
  }
</style>
</head>
<body>
<div class="canvas">
  <div class="panel"></div>
  <div class="band"></div>
  <div class="rail"></div>

  <svg class="chevrons" width="1200" height="1000" aria-hidden="true">
    <g fill="var(--white)">
      <polygon points="287,500 302,541 287,583"/>
      <polygon points="434,500 449,541 434,583"/>
      <polygon points="580,500 595,541 580,583"/>
      <polygon points="726,500 741,541 726,583"/>
      <polygon points="872,500 887,541 872,583"/>
    </g>
  </svg>

  <div class="step" style="left:220px">
    <div class="callout">Any time before OC issued</div>
    <div class="badge">
      <svg width="40" height="56" viewBox="0 0 40 56">
        <text x="20" y="46" text-anchor="middle" font-family="Arimo, Arial, sans-serif" font-weight="700" font-size="50" fill="var(--blue)">$</text>
      </svg>
    </div>
    <div class="label">Lodge 2% Bond</div>
  </div>

  <div class="step" style="left:365px">
    <div class="callout">Within 12 months of completion of building work*</div>
    <div class="badge"><div class="illustration" role="img" aria-label="Illustration of a building inspector in a hard hat"></div></div>
    <div class="label">Developer to appoint building inspector</div>
  </div>

  <div class="step" style="left:511px">
    <div class="callout">Within 15 – 18 months of completion of building work</div>
    <div class="badge">
      <svg width="40" height="48" viewBox="0 0 40 48">
        <path d="M4 2h22l10 10v34H4z" fill="var(--white)" stroke="var(--blue)" stroke-width="2.5"/>
        <path d="M26 2v10h10" fill="none" stroke="var(--blue)" stroke-width="2.5"/>
        <g stroke="var(--blue)" stroke-width="1.6">
          <line x1="9" y1="17" x2="31" y2="17"/><line x1="9" y1="21" x2="31" y2="21"/>
          <line x1="9" y1="25" x2="31" y2="25"/><line x1="9" y1="29" x2="31" y2="29"/>
          <line x1="9" y1="33" x2="31" y2="33"/><line x1="9" y1="37" x2="31" y2="37"/>
          <line x1="9" y1="41" x2="31" y2="41"/>
        </g>
      </svg>
    </div>
    <div class="label">Interim report to be provided</div>
  </div>

  <div class="step" style="left:657px">
    <div class="callout">Within 18 months of&nbsp; completion of building work</div>
    <div class="badge">
      <svg width="62" height="62" viewBox="0 0 62 62">
        <circle cx="31" cy="31" r="27" fill="none" stroke="var(--blue)" stroke-width="6"/>
        <path d="M17 30h7v16h-7z M26 30l7-12c2-3 6-2 5 2l-2 7h9c3 0 4 3 3 5l-3 10c-1 3-3 4-5 4H26z" fill="var(--blue)"/>
      </svg>
    </div>
    <div class="label">Developer to arrange building inspector to carry out final inspection</div>
  </div>

  <div class="step" style="left:803px">
    <div class="callout">21 to 24 months after completion of building work</div>
    <div class="badge">
      <svg width="48" height="52" viewBox="0 0 48 52">
        <path d="M3 8h20l8 8v34H3z" fill="var(--white)" stroke="var(--blue)" stroke-width="2"/>
        <path d="M15 2h20l9 9v32H15z" fill="var(--white)" stroke="var(--blue)" stroke-width="2"/>
        <path d="M35 2v9h9" fill="none" stroke="var(--blue)" stroke-width="2"/>
        <g stroke="var(--blue)" stroke-width="1.5">
          <line x1="19" y1="15" x2="40" y2="15"/><line x1="19" y1="19" x2="40" y2="19"/>
          <line x1="19" y1="23" x2="40" y2="23"/><line x1="19" y1="27" x2="40" y2="27"/>
          <line x1="19" y1="31" x2="40" y2="31"/><line x1="19" y1="35" x2="40" y2="35"/>
        </g>
      </svg>
    </div>
    <div class="label">Final report to be provided</div>
  </div>

  <div class="step" style="left:949px">
    <div class="callout" style="padding-top:14px">2 years after completion of work within 60 days of date of final inspection report (whichever is the later)</div>
    <div class="badge">
      <svg width="46" height="46" viewBox="0 0 46 46">
        <rect x="3" y="7" width="40" height="36" rx="3" fill="var(--white)" stroke="var(--blue)" stroke-width="3"/>
        <rect x="3" y="7" width="40" height="9" fill="var(--blue)"/>
        <g fill="var(--blue)">
          <rect x="10" y="2" width="3" height="9" rx="1.5"/><rect x="18" y="2" width="3" height="9" rx="1.5"/>
          <rect x="26" y="2" width="3" height="9" rx="1.5"/><rect x="34" y="2" width="3" height="9" rx="1.5"/>
        </g>
        <text x="23" y="37" text-anchor="middle" font-family="Arimo, Arial, sans-serif" font-weight="700" font-size="17" fill="var(--blue)">31</text>
      </svg>
    </div>
    <div class="label">Last date for claiming on bond</div>
  </div>
</div>
</body>
</html>
```